An A5, double sided, ticklist

This is for a game at our Pilates + Yoga Studio. A list of things that they need to tick off over the month to earn different points. There are different point categories - a 1 point, 2 point, 5 point and 10 point category.

Under each category is a task they have to complete. ie Under 1 point is: * attend a reformer class * attend a yoga class * attend a sculpt class * follow the studio on Lumigram

Under 2 points is
* do two classes in a row * do a class with a teacher you haven't had in the last month * write a review for your class on Slatewell

Under 3 points is:
* bring a friend or family member to class (not a current member) *wear a piece of studio merch to class * write a Brindlo review

Under 5 points is:
* wear a costume to class and keep it on for the class * have a friend/family member register at the studio as a member this month

Beside each line of a task to complete can there by 3 tick boxes please (ie they can achieve each task 3 times). And then at the end of those tick boxes is space for a total (ie 3 x 2 points = 6).

At the end of each section is their total number of points for that section, and then at the end of the card is the grand total.

It is REQUIRED that this design is made in Canva so that I have access to the design once it's completed so I can add in extra category lines as I think of them.

The caption for the card is Copper Meadow Studio Birthday 2026!

Colours to use are yellow, white + orange. You can see our website here - coppermeadowstudio.example or our Lumigram @copper_meadowstudio to get a feel for the studio + the colours we use!

Thank you!

```html
<!DOCTYPE html>
<html lang="en">
<head>
<meta charset="utf-8">
<title>Copper Meadow Studio Birthday 2026!</title>
<link rel="stylesheet" href="https://fonts.googleapis.com/css2?family=Rammetto+One&family=Poppins:wght@400;500;600&family=Pacifico&display=swap">
<style>
  :root {
    --orange: #e38232;
    --orange-deep: #d0601f;
    --orange-soft: #eeae7c;
    --yellow: #f1be5a;
    --peach: #f8dca8;
    --cream: #fffaf2;
    --white: #ffffff;
    --ink: #141414;
    --taupe: #a69479;
    --brown: #8a7560;
    --stage: #bdbdbd;
    --red: #a8261b;
  }
  * { box-sizing: border-box; margin: 0; padding: 0; }
  html, body { width: 1200px; height: 942px; overflow: hidden; }
  body { background: var(--stage); font-family: "Poppins", sans-serif; position: relative; }

  .card {
    position: absolute; top: 134px; width: 476px; height: 674px; overflow: hidden;
    background: linear-gradient(180deg, var(--white) 0%, var(--white) 45%, var(--peach) 100%);
  }
  .card--front { left: 90px; }
  .card--back { left: 638px; }
  .card .blobs { position: absolute; inset: 0; width: 100%; height: 100%; }

  .brand-mark { position: absolute; text-align: center; color: var(--orange); font-weight: 600; line-height: 1.05; }
  .brand-mark .dot { display: block; width: 14px; height: 14px; border-radius: 50%; background: var(--yellow); margin: 0 auto 5px; }
  .brand-mark span { display: block; font-size: 15px; }

  /* Front */
  .front-title { position: absolute; left: 0; right: 0; text-align: center; }
  .front-kicker { top: 130px; font-family: "Poppins", sans-serif; font-weight: 600; font-size: 25px; color: var(--orange-deep); letter-spacing: 0.5px; }
  .front-name { top: 160px; font-family: "Rammetto One", sans-serif; font-size: 52px; color: var(--ink); letter-spacing: -1px; }
  .front-studio { top: 226px; display: flex; align-items: center; justify-content: center; gap: 16px; font-size: 18px; letter-spacing: 13px; color: var(--ink); }
  .front-studio::before, .front-studio::after { content: ""; width: 64px; height: 1.5px; background: var(--orange-deep); }
  .front-event { top: 256px; font-family: "Rammetto One", sans-serif; font-size: 64px; color: var(--orange); }
  .front-year { top: 322px; font-family: "Rammetto One", sans-serif; font-size: 62px; color: var(--taupe); }
  .figure-art { position: absolute; left: 170px; top: 417px; width: 136px; height: 100px; border-radius: 50px 50px 20px 20px; background: linear-gradient(180deg, rgba(227,130,50,0.08), rgba(227,130,50,0.22)); }
  .front-follow { top: 540px; font-family: "Rammetto One", sans-serif; font-size: 16px; color: var(--brown); }
  .front-handle { top: 566px; font-size: 17px; color: var(--ink); display: flex; justify-content: center; align-items: center; gap: 8px; }
  .front-handle::before { content: ""; width: 13px; height: 13px; border-radius: 3px; background: var(--orange); }
  .front-site { position: absolute; left: 122px; top: 594px; width: 221px; height: 27px; border-radius: 14px; background: var(--orange); color: var(--white); font-size: 11.5px; text-align: center; line-height: 27px; }

  /* Back */
  .back-title { position: absolute; left: 190px; top: 44px; width: 190px; text-align: center; }
  .back-title .script { font-family: "Pacifico", cursive; font-size: 16px; color: var(--orange-deep); }
  .back-title .name { font-family: "Rammetto One", sans-serif; font-size: 18px; color: var(--ink); }
  .back-title .studio { display: flex; align-items: center; justify-content: center; gap: 8px; font-size: 8px; letter-spacing: 6px; color: var(--ink); margin-top: -2px; }
  .back-title .studio::before, .back-title .studio::after { content: ""; width: 32px; height: 1.5px; background: var(--orange-deep); }
  .back-title .event { font-family: "Rammetto One", sans-serif; font-size: 20px; color: var(--orange); line-height: 1.2; }
  .back-title .event b { color: var(--taupe); font-weight: 400; }

  .task-section {
    position: absolute; left: 54px; width: 390px; height: 104px;
    border: 1px solid var(--orange-soft); border-radius: 14px; background: var(--white);
    box-shadow: 0 2px 0 var(--orange-soft);
    padding: 14px 0 0 37px;
  }
  .points-badge {
    position: absolute; left: -26px; top: 25px; width: 54px; height: 55px; border-radius: 9px;
    color: var(--white); text-align: center; font-family: "Rammetto One", sans-serif; padding-top: 8px;
    box-shadow: 0 2px 3px rgba(0,0,0,0.12);
  }
  .points-badge .num { display: block; font-size: 21px; line-height: 1; }
  .points-badge .unit { display: block; font-size: 7.5px; line-height: 1.4; }
  .points-badge--light { background: var(--yellow); }
  .points-badge--bold { background: var(--orange); }

  .task-list { list-style: none; }
  .task { display: grid; grid-template-columns: 227px 54px 56px; align-items: start; margin-bottom: 4px; }
  .task-text { font-size: 10.5px; line-height: 12px; color: var(--ink); padding-left: 13px; position: relative; }
  .task-text::before { content: "★"; position: absolute; left: 0; top: 0; color: var(--orange-deep); font-size: 9px; }
  .tick-boxes { display: flex; gap: 3px; }
  .tick-boxes i { width: 11px; height: 11px; border: 1px solid var(--orange); border-radius: 2px; }
  .task-total { height: 1px; background: var(--orange-soft); margin-top: 8px; margin-left: 0; }

  .section-total { position: absolute; left: 40px; bottom: 14px; display: flex; align-items: center; gap: 6px; font-family: "Rammetto One", sans-serif; font-size: 8.5px; color: var(--brown); }
  .section-total i { width: 88px; height: 13px; border: 1px solid var(--orange); border-radius: 3px; }

  .back-follow { position: absolute; left: 58px; top: 594px; font-family: "Rammetto One", sans-serif; font-size: 12px; color: var(--red); display: flex; gap: 8px; align-items: center; }
  .back-follow::after { content: ""; width: 9px; height: 9px; border-radius: 2px; background: var(--orange); }
  .back-handle { position: absolute; left: 56px; top: 612px; font-size: 11.5px; color: var(--ink); }
  .grand-total { position: absolute; left: 238px; top: 592px; width: 202px; height: 28px; border: 1px solid var(--red); border-radius: 5px; background: var(--white); font-family: "Rammetto One", sans-serif; font-size: 12.5px; color: var(--red); padding: 5px 0 0 9px; }
  .back-site { position: absolute; left: 0; right: 0; top: 636px; text-align: center; font-size: 12px; color: var(--ink); }
  .back-site b { font-weight: 600; }
</style>
</head>
<body>

<section class="card card--front" aria-label="Front of the birthday ticklist card">
  <svg class="blobs" viewBox="0 0 476 674" aria-hidden="true">
    <path d="M0 0 H150 C120 20 110 60 80 90 C55 115 20 105 0 100 Z" fill="#f1be5a"/>
    <path d="M270 0 H476 V160 C430 170 400 120 380 80 C360 40 300 30 270 0 Z" fill="#eeae7c" opacity="0.8"/>
    <path d="M310 0 H476 V165 C440 175 420 140 410 100 C398 55 350 30 310 0 Z" fill="#e38232"/>
    <path d="M0 540 C40 520 80 560 60 600 C45 630 80 650 130 674 H0 Z" fill="#e38232"/>
    <path d="M55 590 C70 620 110 630 130 674 H110 C95 645 60 630 55 590 Z" fill="#ffffff"/>
    <path d="M476 520 C440 520 420 560 410 600 C400 640 350 660 330 674 H476 Z" fill="#f1be5a"/>
    <path d="M476 600 C430 610 420 650 360 674 H476 Z" fill="#e38232"/>
  </svg>

  <div class="brand-mark" style="left:146px; top:58px; width:184px;">
    <b class="dot"></b><span>Copper Meadow</span>
  </div>

  <div class="front-title front-kicker">COPPER</div>
  <div class="front-title front-name">MEADOW</div>
  <div class="front-title front-studio">STUDIO</div>
  <div class="front-title front-event">BIRTHDAY</div>
  <div class="front-title front-year">2026</div>
  <div class="figure-art" role="img" aria-label="Line drawing of a seated meditation pose"></div>
  <div class="front-title front-follow">FOLLOW US ON</div>
  <div class="front-title front-handle">@copper_meadowstudio</div>
  <div class="front-site">www.coppermeadowstudio.example</div>
</section>

<section class="card card--back" aria-label="Back of the birthday ticklist card">
  <svg class="blobs" viewBox="0 0 476 674" aria-hidden="true">
    <path d="M0 0 H120 C130 30 100 45 70 60 C40 75 30 100 0 110 Z" fill="#e38232"/>
    <path d="M0 40 C40 20 90 40 80 80 C70 110 30 105 0 105 Z" fill="#f1be5a"/>
    <path d="M350 0 H476 V85 C440 60 410 60 390 40 C375 25 365 10 350 0 Z" fill="#f6d49a"/>
    <path d="M390 0 H476 V105 C445 95 420 70 410 40 C405 20 395 10 390 0 Z" fill="#e38232"/>
    <path d="M0 580 C30 590 40 630 70 650 C90 665 100 674 100 674 H0 Z" fill="#e38232"/>
    <path d="M0 620 C30 630 70 650 90 674 H0 Z" fill="#f1be5a"/>
    <path d="M476 610 C440 630 420 660 370 674 H476 Z" fill="#e38232"/>
  </svg>

  <div class="brand-mark" style="left:84px; top:52px; width:92px;">
    <b class="dot"></b><span>Copper</span><span>Meadow</span>
  </div>

  <div class="back-title">
    <div><span class="script">Copper</span> <span class="name">MEADOW</span></div>
    <div class="studio">STUDIO</div>
    <div class="event">BIRTHDAY <b>2026</b></div>
  </div>

  <div class="task-section" style="top:129px;">
    <div class="points-badge points-badge--light"><span class="num">01</span><span class="unit">POINT</span></div>
    <ul class="task-list">
      <li class="task"><span class="task-text">Attend a reformer class</span><span class="tick-boxes"><i></i><i></i><i></i></span><span class="task-total"></span></li>
      <li class="task"><span class="task-text">Attend a yoga class</span><span class="tick-boxes"><i></i><i></i><i></i></span><span class="task-total"></span></li>
      <li class="task"><span class="task-text">Attend a sculpt class</span><span class="tick-boxes"><i></i><i></i><i></i></span><span class="task-total"></span></li>
      <li class="task"><span class="task-text">Follow the studio on Lumigram</span><span class="tick-boxes"><i></i><i></i><i></i></span><span class="task-total"></span></li>
    </ul>
    <div class="section-total">SECTION TOTAL <i></i></div>
  </div>

  <div class="task-section" style="top:246px;">
    <div class="points-badge points-badge--bold"><span class="num">02</span><span class="unit">POINT</span></div>
    <ul class="task-list">
      <li class="task"><span class="task-text">Do two classes in a row</span><span class="tick-boxes"><i></i><i></i><i></i></span><span class="task-total"></span></li>
      <li class="task"><span class="task-text">Do a class with a teacher you haven't had in the last month</span><span class="tick-boxes"><i></i><i></i><i></i></span><span class="task-total"></span></li>
      <li class="task"><span class="task-text">Write a review for your class on Slatewell</span><span class="tick-boxes"><i></i><i></i><i></i></span><span class="task-total"></span></li>
    </ul>
    <div class="section-total">SECTION TOTAL <i></i></div>
  </div>

  <div class="task-section" style="top:366px;">
    <div class="points-badge points-badge--light"><span class="num">03</span><span class="unit">POINT</span></div>
    <ul class="task-list">
      <li class="task"><span class="task-text">Bring a friend or family member to class (not a current member)</span><span class="tick-boxes"><i></i><i></i><i></i></span><span class="task-total"></span></li>
      <li class="task"><span class="task-text">Wear a piece of studio merch to class</span><span class="tick-boxes"><i></i><i></i><i></i></span><span class="task-total"></span></li>
      <li class="task"><span class="task-text">Write a Brindlo review</span><span class="tick-boxes"><i></i><i></i><i></i></span><span class="task-total"></span></li>
    </ul>
    <div class="section-total">SECTION TOTAL <i></i></div>
  </div>

  <div class="task-section" style="top:481px;">
    <div class="points-badge points-badge--bold"><span class="num">05</span><span class="unit">POINT</span></div>
    <ul class="task-list">
      <li class="task"><span class="task-text">wear a costume to class and keep it on for the class</span><span class="tick-boxes"><i></i><i></i><i></i></span><span class="task-total"></span></li>
      <li class="task"><span class="task-text">have a friend/family member register at the studio as a member this month</span><span class="tick-boxes"><i></i><i></i><i></i></span><span class="task-total"></span></li>
    </ul>
    <div class="section-total">SECTION TOTAL <i></i></div>
  </div>

  <div class="back-follow">FOLLOW US ON</div>
  <div class="back-handle">@copper_meadowstudio</div>
  <div class="grand-total">GRAND TOTAL</div>
  <div class="back-site">www.<b>coppermeadowstudio</b>.example</div>
</section>

</body>
</html>
```